Talvo shoes is a wholesale shoe sales company , mostly working in female shoes and kiddies shoes with a small mens section . looking for a clean slick look. http://www.kemrafootwear.co.za/shop/ is a good reference

It Company

```html
<!DOCTYPE html>
<html lang="en">
<head>
<meta charset="utf-8">
<title>Talvo shoes – Home</title>
<link href="https://fonts.googleapis.com/css2?family=Source+Sans+3:wght@400;600;700&family=Pinyon+Script&display=swap" rel="stylesheet">
<style>
:root{
  --paper:#f3efe8;
  --purple:#8b7ba1;
  --purple-dark:#6f5d88;
  --teal:#1d4d55;
  --band:#4a727a;
  --ink:#2a2a2a;
  --muted:#666;
  --card:#ffffff;
}
*{box-sizing:border-box;margin:0;padding:0}
html,body{width:815px;height:1200px;overflow:hidden}
body{background:var(--paper);font-family:"Source Sans 3",sans-serif;font-weight:400;color:var(--ink);position:relative}
.abs{position:absolute}
.brand{left:128px;top:22px;font-size:38px;font-weight:400;color:#111;letter-spacing:-1px}
.tagline{left:139px;top:84px;font-size:15px;color:#222}
.account{left:492px;top:25px;font-size:13px}
.account .sep{display:inline-block;width:1px;height:16px;background:#999;vertical-align:middle;margin:0 6px}
.cart{left:620px;top:25px;font-size:13px;display:flex;align-items:center;gap:4px}
.phone{left:586px;top:78px;font-size:13.5px;font-weight:600;display:flex;align-items:center;gap:3px}
.nav{left:82px;top:119px;width:651px;height:33px;background:var(--purple);border-radius:3px;display:flex;align-items:center}
.nav a{color:#fff;text-decoration:none;font-weight:600;font-size:13.5px;height:33px;line-height:33px;padding:0 14px;border-right:1px solid #a598b7}
.nav a:first-child{color:#1b1b1b;padding-left:48px}
.nav a:last-child{border-right:none}
.search{position:absolute;right:10px;top:10px;width:122px;height:14px;background:#fff;border-radius:7px;font-size:5px;color:#999;line-height:14px;padding-left:15px}
.search svg{position:absolute;right:14px;top:3px}
.hero{left:82px;top:161px;width:652px;height:208px;box-shadow:0 12px 10px -8px rgba(0,0,0,.25)}
.hero-panel{position:absolute;left:0;top:0;width:228px;height:208px;background:#e0e3e7}
.hero-photo{position:absolute;left:228px;top:0;width:424px;height:208px;
  background:linear-gradient(180deg,rgba(243,243,244,0) 45%,rgba(214,168,136,.55) 70%,rgba(236,236,238,0) 92%),
             linear-gradient(90deg,#d5d9de 0%,#eceef0 40%,#f4f4f4 100%)}
.hero-title{position:absolute;left:32px;top:28px;font-family:"Pinyon Script",cursive;font-size:29px;color:#333}
.hero-text{position:absolute;left:32px;top:72px;width:205px;font-size:8.5px;line-height:11.5px;color:#666;font-weight:400}
.shop-btn{position:absolute;left:68px;top:125px;width:133px;height:33px;background:var(--teal);color:#fff;font-size:18px;text-align:center;line-height:33px;border-radius:2px}
.dots{position:absolute;left:514px;top:194px;display:flex;gap:4px}
.dots i{width:8px;height:8px;border-radius:50%;background:#888;display:block}
.dots i.on{background:var(--purple-dark)}
.cats{left:83px;top:437px;width:141px;background:#fff;box-shadow:0 1px 3px rgba(0,0,0,.25)}
.cats h3{background:var(--teal);color:#fff;font-size:12px;font-weight:700;height:26px;line-height:26px;padding-left:13px}
.cats li{list-style:none;height:21px;line-height:21px;font-size:10px;font-weight:400;color:#444;padding-left:21px;border-bottom:1px solid #ddd;position:relative}
.cats li.active{background:var(--purple-dark);color:#fff;border-left:4px solid #4a3a60;padding-left:17px}
.cats li.active::after{content:"›";position:absolute;right:5px;font-size:9px}
.label{font-size:7.5px;color:#333;font-weight:400}
.card{width:126px;height:158px;background:var(--card);box-shadow:0 1px 3px rgba(0,0,0,.2)}
.card .pic{height:98px;margin:0 4px}
.red{background:linear-gradient(180deg,#fff 8%,#f1d3d3 45%,#e7b7b7 70%,#fff 96%)}
.blue{background:linear-gradient(180deg,#fff 8%,#d3dcef 45%,#c2cbe6 70%,#fff 96%)}
.orange{background:linear-gradient(180deg,#fff 20%,#f5dcc6 55%,#efcaa8 72%,#fff 94%)}
.card .row{display:flex;align-items:center;justify-content:space-between;padding:0 8px;margin-top:8px;font-size:10px;color:#333}
.qty{display:flex;align-items:center;gap:5px;font-size:4px;color:#aaa}
.qty-field{width:35px;height:15px;border:1px solid #ccc;font-size:9px;color:#333;line-height:13px;padding-left:8px;position:relative;display:block}
.qty-field svg{position:absolute;right:3px;top:2px}
.add{margin:7px 8px 0;height:19px;background:var(--purple);color:#fff;font-size:6px;font-weight:700;display:flex;align-items:center;justify-content:center;gap:4px}
.social{left:93px;top:698px;display:flex;gap:10px}
.social .b{width:33px;text-align:center}
.social .count{height:23px;border:1px solid #bbb;background:#fff;font-size:9px;font-weight:600;line-height:21px;border-radius:2px}
.social .act{height:14px;margin-top:7px;font-size:6px;font-weight:700;color:#fff;line-height:14px}
.divider{left:143px;top:916px;width:529px;height:1px;background:#cfc9c0}
.info-box{top:968px;width:183px;height:129px;border:1px solid #cdc7bf;padding:12px 8px}
.info-box h4{font-size:14px;font-weight:600;color:#333;margin-bottom:8px}
.info-box h4 em{font-style:normal;color:var(--purple-dark)}
.info-box p{font-size:7.5px;line-height:12px;color:#555;font-weight:400}
.more{margin-top:8px;font-size:10px;color:var(--purple-dark);font-weight:600}
.nl{display:flex;margin-top:20px}
.nl span{width:108px;height:21px;background:#ebe7e1;font-size:7px;font-style:italic;color:#999;line-height:21px;padding-left:3px}
.nl b{width:47px;height:21px;background:var(--purple);color:#fff;font-size:10px;font-weight:600;line-height:21px;text-align:center}
.links li{list-style:none;font-size:8px;font-weight:400;color:#333;display:flex;align-items:center;gap:13px;height:19.5px;padding-left:18px}
.links li i{width:12px;height:12px;border-radius:50%;background:#111;display:block}
.links li.soft i{background:#9a8bb0}
.links li.soft{color:var(--purple-dark)}
.footer{left:0;top:1148px;width:815px;height:52px;background:var(--band);color:#fff;font-size:9.5px;text-align:center;line-height:52px}
</style>
</head>
<body>
<div class="abs brand">Talvo shoes</div>
<div class="abs tagline">Your tagline here</div>
<div class="abs account">Log in<span class="sep"></span>Register</div>
<div class="abs cart">My cart
<svg width="18" height="14" viewBox="0 0 18 14"><path d="M1 1h3l2 8h9l2-6H5" fill="none" stroke="#8b7ba1" stroke-width="1.4"/><circle cx="7" cy="12" r="1.3" fill="#8b7ba1"/><circle cx="14" cy="12" r="1.3" fill="#8b7ba1"/></svg>($0.00)</div>
<div class="abs phone"><svg width="15" height="15" viewBox="0 0 15 15"><rect width="15" height="15" rx="2" fill="#8b7ba1"/><path d="M5 3c-1 1-1 3 1 6s4 4 5 3l-1.5-2-1.5 1c-1-.5-2-2-2.5-3l1-1.5z" fill="#fff"/></svg>Call Us 021-555-0148</div>

<nav class="abs nav">
<a>HOME</a><a>LADIES</a><a>MENS</a><a>KIDS</a><a>CONTACT US</a>
<div class="search">Search...<svg width="7" height="7" viewBox="0 0 7 7"><circle cx="3" cy="3" r="2" fill="none" stroke="#888"/><path d="M4.5 4.5l2 2" stroke="#888"/></svg></div>
</nav>

<section class="abs hero">
<div class="hero-panel"></div>
<div class="hero-photo" role="img" aria-label="Photo of crossed legs wearing black high-heeled shoes in a bright white room"></div>
<div class="hero-title">Lorem ipsum Dolor</div>
<p class="hero-text">Lorem ipsum is a dummy text only. Dolor sit amet, consectetur adipiscing elit. Nullam felis mauris, eleifend ac rhoncus non, lobortis at diam.</p>
<div class="shop-btn">Shop Now</div>
<div class="dots"><i></i><i class="on"></i><i></i><i></i></div>
</section>

<aside class="abs cats">
<h3>Product Categories</h3>
<ul>
<li>Pellentesque</li><li>Accumsan</li><li>Dignissim</li><li class="active">Libero eu</li><li>Dignissim.</li><li>Aliquam sed</li><li style="border-bottom:none">accumsan tortor</li>
</ul>
</aside>

<div class="abs label" style="left:262px;top:440px">Name of the product</div>
<div class="abs label" style="left:420px;top:440px">Name of the product</div>
<div class="abs label" style="left:571px;top:440px">Name of the product</div>
<div class="abs label" style="left:262px;top:672px">Name of the product</div>
<div class="abs label" style="left:420px;top:672px">Name of the product</div>
<div class="abs label" style="left:571px;top:672px">Name of the product</div>

<div class="abs card" style="left:262px;top:455px"><div class="pic red" role="img" aria-label="Red suede high-heeled pumps"></div><div class="row">$18.00<span class="qty">QTY:<span class="qty-field">1<svg width="5" height="9" viewBox="0 0 5 9"><path d="M0 3.5L2.5 0 5 3.5zM0 5.5L2.5 9 5 5.5z" fill="#333"/></svg></span></span></div><div class="add">▣ ADD TO CART</div></div>
<div class="abs card" style="left:420px;top:455px"><div class="pic blue" role="img" aria-label="Blue and teal platform sandals"></div><div class="row">$18.00<span class="qty">QTY:<span class="qty-field">1<svg width="5" height="9" viewBox="0 0 5 9"><path d="M0 3.5L2.5 0 5 3.5zM0 5.5L2.5 9 5 5.5z" fill="#333"/></svg></span></span></div><div class="add">▣ ADD TO CART</div></div>
<div class="abs card" style="left:571px;top:455px"><div class="pic orange" role="img" aria-label="Orange patent heels"></div><div class="row">$18.00<span class="qty">QTY:<span class="qty-field">1<svg width="5" height="9" viewBox="0 0 5 9"><path d="M0 3.5L2.5 0 5 3.5zM0 5.5L2.5 9 5 5.5z" fill="#333"/></svg></span></span></div><div class="add">▣ ADD TO CART</div></div>
<div class="abs card" style="left:262px;top:688px"><div class="pic red" role="img" aria-label="Red suede high-heeled pumps"></div><div class="row">$18.00<span class="qty">QTY:<span class="qty-field">1<svg width="5" height="9" viewBox="0 0 5 9"><path d="M0 3.5L2.5 0 5 3.5zM0 5.5L2.5 9 5 5.5z" fill="#333"/></svg></span></span></div><div class="add">▣ ADD TO CART</div></div>
<div class="abs card" style="left:420px;top:688px"><div class="pic blue" role="img" aria-label="Blue and teal platform sandals"></div><div class="row">$18.00<span class="qty">QTY:<span class="qty-field">1<svg width="5" height="9" viewBox="0 0 5 9"><path d="M0 3.5L2.5 0 5 3.5zM0 5.5L2.5 9 5 5.5z" fill="#333"/></svg></span></span></div><div class="add">▣ ADD TO CART</div></div>
<div class="abs card" style="left:571px;top:688px"><div class="pic orange" role="img" aria-label="Orange patent heels"></div><div class="row">$18.00<span class="qty">QTY:<span class="qty-field">1<svg width="5" height="9" viewBox="0 0 5 9"><path d="M0 3.5L2.5 0 5 3.5zM0 5.5L2.5 9 5 5.5z" fill="#333"/></svg></span></span></div><div class="add">▣ ADD TO CART</div></div>

<div class="abs social">
<div class="b"><div class="count">868</div><div class="act" style="background:#2ea9e0">Share</div></div>
<div class="b"><div class="count">1.3K</div><div class="act" style="background:#3d5a98">Like</div></div>
<div class="b"><div class="count">28</div><div class="act" style="background:#444">+1</div></div>
</div>

<div class="abs divider"></div>

<div class="abs info-box" style="left:87px">
<h4>About <em>Talvo shoes</em></h4>
<p>Lorem ipsum is a dummy text only. Dolor sit amet, consectetur adipiscing elit. Nullam felis mauris, eleifend ac rhoncus non, lobortis at diam.</p>
<div class="more">Read more &nbsp;»</div>
</div>
<div class="abs info-box" style="left:310px">
<h4>Sign-up to our newsletter</h4>
<p>Lorem ipsum is a dummy text only.<br>Dolor sit amet, consectetur<br>adipiscing elit</p>
<div class="nl"><span>Enter email address</span><b>Submit</b></div>
</div>
<div class="abs info-box" style="left:510px">
<h4 style="padding-left:16px">Keep Connected</h4>
<ul class="links">
<li><i></i>Like us on Friendly</li>
<li><i></i>Follow us on Chirper</li>
<li class="soft"><i></i>Add us on Circlet</li>
<li><i></i>Follow us on ProLink</li>
</ul>
</div>

<footer class="abs footer">Copyright©Talvo shoes. All Rights Reserved. 2014</footer>
</body>
</html>
```